We Need a Letterhead + Fax Cover Sheet for Kestrel Works

LETTERHEAD:
- Simple letterhead. Please provide an editable .doc file apart from usual Source Files. Logo Files attached for your use.
- Please place our logo on the upper right corner of the page. You may add some sort of graphic, or light colored background (depends on what looks good).
- Footer should include:
Kestrel Works, LLC
418 Wrenfield Ave. Suite 172
Mobile, AL 36619

FAX COVER SHEET:
- Have the logo placed here, should be large, maybe an eight of the page.
- Put:
From:
To:
Phone Number:
Fax Number:

*Still needs some details, will update you because working on the website, etc.

Kestrel Harbor Staffing Services

```html
<!DOCTYPE html>
<html lang="en">
<head>
<meta charset="utf-8">
<title>Kestrel Works – Letterhead + Fax Cover Sheet</title>
<link href="https://fonts.googleapis.com/css2?family=Lato:wght@400;700&family=Montserrat:wght@500&family=Work+Sans:wght@300;400&display=swap" rel="stylesheet">
<style>
  :root {
    --board: #e0dfe0;
    --paper: #ffffff;
    --brand-blue: #1a6fa8;
    --brand-green: #8aa53a;
    --ink: #333333;
    --ink-soft: #4a4a4a;
    --field-bg: #f1f1f3;
    --signature-tone: #c9c9cc;
  }
  * { box-sizing: border-box; margin: 0; padding: 0; }
  html, body { width: 1200px; height: 978px; overflow: hidden; background: var(--board); }
  .board { position: relative; width: 1200px; height: 978px; }

  .board-title {
    position: absolute; top: 92px; left: 0; width: 100%;
    text-align: center;
    font-family: "Montserrat", sans-serif; font-weight: 500;
    font-size: 44px; letter-spacing: 1.5px; color: var(--brand-blue);
  }

  .sheet {
    position: absolute; top: 211px; width: 497px; height: 703px;
    background: var(--paper);
    box-shadow: 4px 6px 10px rgba(0,0,0,0.18);
  }
  .sheet--letter { left: 73px; }
  .sheet--fax { left: 632px; width: 495px; }

  .company-name {
    position: absolute;
    font-family: "Work Sans", sans-serif; font-weight: 400;
    font-size: 22px; color: var(--brand-blue);
    padding-bottom: 3px; border-bottom: 1px solid var(--brand-green);
    width: 237px; white-space: nowrap;
  }
  .company-address {
    position: absolute;
    font-family: "Work Sans", sans-serif; font-size: 10.5px;
    color: var(--ink-soft); letter-spacing: 0.3px; white-space: nowrap;
  }
  .sheet--letter .company-name { left: 48px; top: 27px; }
  .sheet--letter .company-address { left: 48px; top: 64px; }
  .sheet--fax .company-name { left: 26px; top: 32px; }
  .sheet--fax .company-address { left: 26px; top: 69px; }

  .brand-mark {
    position: absolute; display: flex; flex-direction: column; align-items: center; justify-content: center;
    gap: 8px; text-align: center;
    font-family: "Work Sans", sans-serif; font-weight: 400; color: var(--brand-blue);
  }
  .brand-mark__dot { border-radius: 50%; background: var(--brand-green); }
  .sheet--letter .brand-mark { left: 343px; top: 26px; width: 120px; height: 127px; font-size: 13px; line-height: 1.2; }
  .sheet--letter .brand-mark__dot { width: 34px; height: 34px; }
  .sheet--fax .brand-mark { left: 326px; top: 29px; width: 146px; height: 156px; font-size: 15px; line-height: 1.2; }
  .sheet--fax .brand-mark__dot { width: 42px; height: 42px; }

  .letter-body {
    position: absolute; left: 34px; top: 234px; width: 430px;
    font-family: "Lato", sans-serif; color: var(--ink);
  }
  .letter-salutation { font-size: 11.5px; margin-bottom: 19px; }
  .letter-paragraph { font-size: 9.9px; line-height: 13px; color: var(--ink-soft); margin-bottom: 16px; }
  .letter-closing { position: absolute; left: 34px; top: 514px; font-family: "Lato", sans-serif; color: var(--ink); }
  .letter-closing__regards { font-size: 11.5px; margin-bottom: 6px; }
  .letter-closing__name { font-size: 11.5px; }
  .letter-closing__role { font-size: 8px; font-weight: 700; margin-top: 1px; }
  .letter-closing__signature { width: 90px; height: 12px; margin-top: 11px; background: var(--signature-tone); border-radius: 2px; }

  .fax-panel {
    position: absolute; left: 26px; top: 229px; width: 443px; height: 315px;
    background: var(--field-bg);
    font-family: "Lato", sans-serif; color: var(--ink);
  }
  .fax-panel__title { position: absolute; left: 13px; top: 22px; font-size: 38px; font-weight: 400; }
  .fax-field {
    position: absolute; left: 16px; width: 415px;
    display: flex; align-items: flex-end; font-size: 11px;
  }
  .fax-field__line { flex: 1; border-bottom: 1px solid var(--ink); height: 10px; }
</style>
</head>
<body>
<main class="board">
  <h1 class="board-title">Letterhead + Fax Cover Sheet</h1>

  <section class="sheet sheet--letter">
    <div class="company-name">Kestrel Works, LLC</div>
    <div class="company-address">418 Wrenfield Ave. Suite 172 Mobile, AL 36619</div>
    <div class="brand-mark">
      <span class="brand-mark__dot"></span>
      <span>Kestrel Harbor Staffing Services</span>
    </div>

    <div class="letter-body">
      <p class="letter-salutation">Dear sir/Madam,</p>
      <p class="letter-paragraph">Lorem ipsum dolor sit amet, an vel recteque dissentiet, detracto albucius platonem ex vel, eros repudiandae cu. Atqui aliquando nec an, unum graece adolescens vel ad. Id odio scae has, iudico euismod atomorum ius ea, cum ea honestatis quaerendum theophrastus. Mea honestatis quaerendum theophrastus. Mea</p>
      <p class="letter-paragraph">Lorem ipsum dolor sit amet, an vel recteque dissentiet, detracto albucius platonem ex vel, eros repudiandae cu. Atqui aliquando nec an, unum graece adolescens vel ad. Id odio scae has, iudico euismod atomorum ius ea, cum ea honestatis quaerendum theophrastus. Mea doming repudiandae ex, cu cum civibus assentior posidonium. Quo etiam pertinax ex, te eros repudiandae cu. Atqui aliquando nec an, unum graece adolescens vel ad. Id odio scae honestatis quaerendum theophrastus. Mea</p>
      <p class="letter-paragraph">Lorem ipsum dolor sit amet, an vel recteque dissentiet, detracto albucius platonem ex vel, eros repudiandae cu. Atqui aliquando nec an, unum graece adolescens vel ad. Id odio scae has, iudico euismod atomorum ius ea, cum ea honestatis quaerendum theophrastus. Mea honestatis quaerendum theophrastus. Mea</p>
    </div>

    <div class="letter-closing">
      <p class="letter-closing__regards">Kind Regards</p>
      <p class="letter-closing__name">Daniel Whitmore</p>
      <p class="letter-closing__role">Chief Alchemist</p>
      <div class="letter-closing__signature" role="img" aria-label="Handwritten signature of Daniel Whitmore"></div>
    </div>
  </section>

  <section class="sheet sheet--fax">
    <div class="company-name">Kestrel Works, LLC</div>
    <div class="company-address">418 Wrenfield Ave. Suite 172 Mobile, AL 36619</div>
    <div class="brand-mark">
      <span class="brand-mark__dot"></span>
      <span>Kestrel Harbor Staffing Services</span>
    </div>

    <div class="fax-panel">
      <h2 class="fax-panel__title">Fax</h2>
      <div class="fax-field" style="top:100px"><span>From:</span><span class="fax-field__line"></span></div>
      <div class="fax-field" style="top:157px"><span>To:</span><span class="fax-field__line"></span></div>
      <div class="fax-field" style="top:212px"><span>Phone:</span><span class="fax-field__line"></span></div>
      <div class="fax-field" style="top:267px"><span>Fax:</span><span class="fax-field__line"></span></div>
    </div>
  </section>
</main>
</body>
</html>
```